Thornfield Marsh, LLC Website

We are a small law firm in need of a website that contains the following:
1. Attractive main page
2. About us/attorney info for three people: Leonard Thornfield (attorney), Brent Marsh (attorney), and Melinda Carrow (legal assistant). We have bio's ready to submit.
3. Blog/video page. We'd like to post blogs and videos to help drive traffic
4. Multidistrict Litigation and Class Actions page, where we post information regarding active MDLs and Class actions that we are doing intake on.
Updates

Can you also please use the color "gold" in the design and logo? Thanks.

Industry/Entity Type

Legal

Coding

Coded - Design and coding required

Number of Pages Required

1 page

Colors
0054AA
0677BA
7BADD7
CADEEF
E8F1F8

Requirements
Must have
• 1. Attractive main page 2. About us/attorney info for three people: Leonard Thornfield (attorney), Brent Marsh (attorney), and Melinda Carrow (legal assistant). We have bio's ready to submit. 3. Blog/video page. We'd like to post blogs and videos to help drive traffic 4. Multidistrict Litigation and Class Actions page, where we post information regarding active MDLs and Class actions that we are doing intake on.

```html
<!DOCTYPE html>
<html lang="en">
<head>
<meta charset="utf-8">
<title>Thornfield Marsh, LLC — Lawyers</title>
<link href="https://fonts.googleapis.com/css2?family=Poppins:wght@400;500;600&family=Montserrat:wght@400;500&display=swap" rel="stylesheet">
<style>
:root{
  --gold:#b98e56;
  --gold-dark:#a67c47;
  --navy:#16244a;
  --ink:#222;
  --muted:#555;
  --cream:#f7efe6;
  --line:#e5e0da;
  --white:#fff;
}
*{box-sizing:border-box;margin:0;padding:0}
html,body{width:1200px;height:3816px;overflow:hidden}
body{font-family:"Poppins",sans-serif;color:var(--ink);background:var(--white);position:relative}
.abs{position:absolute}
.eyebrow{color:var(--gold);font-size:15px;font-weight:500;text-transform:uppercase}
.section-title{font-size:36px;font-weight:500;text-transform:uppercase;color:#1d1d1d;letter-spacing:.5px}
.center{text-align:center;width:1200px;left:0}
.body-text{font-family:"Montserrat",sans-serif;font-size:13px;line-height:22.5px;color:var(--muted)}
.btn{display:flex;align-items:center;height:44px;border:2px solid var(--gold);background:var(--white);font-size:14px;font-weight:500;color:#222}
.btn .mark{width:48px;height:100%;background:var(--gold)}
.btn span{padding:0 20px 0 18px}
/* header */
.header{top:0;left:0;width:1200px;height:104px;background:var(--white)}
.logo{display:flex;align-items:center;gap:12px;border:3px solid var(--gold);height:60px;padding-right:14px}
.logo .sq{width:80px;height:100%;background:var(--gold)}
.logo b{font-size:27px;font-weight:600;color:var(--navy)}
.call{top:10px;left:834px;height:44px;width:254px;border:2px solid var(--gold);display:flex;align-items:center;font-size:16px}
.call .ic{width:50px;height:100%;background:var(--gold);display:flex;align-items:center;justify-content:center;margin-right:14px}
.nav{top:72px;left:548px;display:flex;gap:31px;font-size:13px;font-weight:500;text-transform:uppercase;color:#333}
.nav .on{color:var(--gold)}
/* hero */
.hero{top:104px;left:0;width:1200px;height:628px;background:linear-gradient(180deg,#0f2431 0%,#1b2f38 55%,#2a2a26 100%)}
.hero-copy{top:90px;color:var(--white)}
.hero-copy h3{font-size:21px;font-weight:500}
.hero-copy h1{font-size:58px;font-weight:600;margin-top:0;line-height:72px}
.hero-copy p{font-size:15px;font-weight:500;line-height:26px;width:580px;margin:8px auto 0}
.hero-btn{left:508px;top:266px;border-color:var(--gold);background:var(--navy);color:var(--white)}
.dots{left:1124px;top:520px;display:flex;flex-direction:column;gap:8px}
.dots i{width:12px;height:12px;border:2px solid #fff;border-radius:50%}
.dots i.on{border-color:var(--gold)}
/* about */
.about-block{top:702px;left:76px;width:450px;height:579px;background:var(--gold)}
.about-photo{top:634px;left:138px;width:483px;height:579px;background:linear-gradient(160deg,#cfe0ea,#7f97ab 55%,#1f2f47)}
.about-copy{top:780px;left:659px;width:422px}
.about-copy h2{font-size:36px;font-weight:500;color:#222;margin:6px 0 22px}
.about-copy p{text-align:justify;margin-bottom:22px}
/* attorneys */
.attorneys{top:1351px;left:0;width:1200px;height:596px;background:linear-gradient(180deg,#f6ece0,#fbf6f0 60%,#f2e8dc)}
.card{top:147px;width:308px;height:355px;background:var(--navy);color:var(--white);text-align:center}
.card.gold{background:var(--gold);height:391px}
.portrait{width:204px;height:204px;border-radius:50%;border:6px solid var(--gold);margin:40px auto 0;background:linear-gradient(160deg,#e6e2dc,#9aa2ae)}
.card.gold .portrait{border-color:#a47840}
.card h4{font-size:16px;font-weight:600;margin-top:30px;text-transform:uppercase}
.card .role{font-size:15px;color:var(--gold);margin-top:4px}
.card.gold .role{color:#222}
.socials{display:flex;gap:6px;justify-content:center;margin-top:12px}
.socials i{width:24px;height:24px;border:1.5px solid #fff;border-radius:50%}
.plus{width:38px;height:38px;border-radius:50%;background:var(--gold);color:#fff;font-size:24px;line-height:36px;left:135px;bottom:-19px}
.card.gold .plus{background:var(--navy)}
/* litigation */
.lit{top:1947px;left:0;width:1200px;height:474px;background:var(--gold)}
.lit-photo{top:0;left:0;width:1200px;height:474px}
.lit-copy{top:70px;left:111px;width:486px;color:var(--white)}
.lit-copy h6{font-size:15px;font-weight:500}
.lit-copy h2{font-size:29px;font-weight:500;margin:8px 0 22px}
.lit-copy p{color:#fff;text-align:justify}
.lit-btn{top:354px;left:111px;border-color:var(--white);border-width:3px}
.lit-btn .mark{background:var(--navy)}
/* blog */
.post{top:2556px;width:307px;height:417px;background:var(--white)}
.post .img{height:237px;background:linear-gradient(160deg,#c9a57a,#5b4a3a)}
.post .box{margin:0 10px;border:1px solid var(--line);border-top:none;height:180px;padding-top:18px;text-align:center;position:relative;top:-10px;background:var(--white)}
.post .date{color:var(--gold);font-size:17px;font-weight:500}
.post h5{font-size:16px;font-weight:600;margin:9px 0 10px;color:#222}
.post p{font-size:13px;line-height:22px;color:var(--muted);padding:0 22px}
.post .meta{position:absolute;left:0;right:0;bottom:0;height:44px;border-top:1px solid var(--line);display:flex;align-items:center;justify-content:space-between;padding:0 14px 0 16px;font-size:12px;color:#888}
.post .meta i{width:34px;height:32px;border:1px solid var(--line);display:flex;align-items:center;justify-content:center}
/* testimonials */
.testi{top:3040px;left:0;width:1200px;height:409px;background:linear-gradient(180deg,#f8f1e9,#fbf7f2)}
.quote{top:145px;width:474px;height:208px;background:var(--white);box-shadow:0 2px 8px rgba(0,0,0,.06);padding:30px 30px 0 32px}
.quote p{font-size:14px;line-height:26px;color:var(--muted);text-align:justify}
.quote .who{display:flex;align-items:center;gap:14px;margin:14px 0 0 -32px;font-size:15px;font-weight:500}
.quote .who::before{content:"";width:52px;height:1px;background:var(--gold)}
.stars{color:#e0a52a;font-size:13px;margin-left:66px;letter-spacing:1px}
.qmark{right:26px;bottom:0;font-size:140px;line-height:110px;color:#eeeeee;font-family:Georgia,serif;height:60px;overflow:hidden}
.arrow{top:232px;width:34px;height:34px;border:1.5px solid #aaa;border-radius:50%;display:flex;align-items:center;justify-content:center}
/* footer */
.footer{top:3449px;left:0;width:1200px;height:367px;background:var(--navy);color:var(--white)}
.footer h3{font-size:20px;font-weight:500;text-transform:uppercase}
.field{height:36px;background:var(--white);color:#555;font-size:11px;padding:11px 12px}
.submit{top:235px;left:114px;width:98px;height:34px;background:var(--gold);font-size:14px;font-weight:600;text-align:center;line-height:34px}
.c-item{left:554px;display:flex;gap:14px}
.c-item .ic{width:44px;height:44px;border:2px solid #fff;border-radius:50%;display:flex;align-items:center;justify-content:center}
.c-item b{font-size:16px;font-weight:500;display:block}
.c-item span{font-size:13px;line-height:19px}
.flogo{top:80px;left:804px;width:285px;height:52px;border:3px solid var(--gold);background:var(--white);display:flex;align-items:center;gap:10px;padding-right:10px}
.flogo .sq{width:62px;height:100%;background:var(--gold)}
.flogo b{color:var(--navy);font-size:20px;font-weight:600}
.fsoc{top:186px;left:846px;display:flex;gap:9px}
.fsoc i{width:33px;height:33px;border:1.5px solid #fff;border-radius:50%}
.copy{top:322px;font-size:14px}
</style>
</head>
<body>

<header class="header abs">
  <div class="logo abs" style="top:22px;left:111px"><div class="sq"></div><b>THORNFIELD MARSH, LLC</b></div>
  <div class="call abs"><div class="ic"><svg width="18" height="18" viewBox="0 0 24 24"><path fill="#fff" d="M6.6 10.8a15 15 0 0 0 6.6 6.6l2.2-2.2c.3-.3.7-.4 1-.2 1.1.4 2.3.6 3.6.6.6 0 1 .4 1 1V20c0 .6-.4 1-1 1A17 17 0 0 1 3 4c0-.6.4-1 1-1h3.5c.6 0 1 .4 1 1 0 1.3.2 2.5.6 3.6.1.3 0 .7-.2 1z"/></svg></div>Call Us : 555-018-2746</div>
  <nav class="nav abs"><span class="on">Home</span><span>About Us</span><span>Attorney</span><span>Blog</span><span>Class Actions</span><span>Contact Us</span></nav>
</header>

<section class="hero abs" role="img" aria-label="Lawyer seated at a desk in a dim library lined with bookshelves">
  <div class="hero-copy abs center">
    <h3>WELCOME TO</h3>
    <h1>THORNFIELD MARSH, LLC</h1>
    <p>Nemo enim ipsam voluptatem quia voluptas sit aspernatur aut odit aut fugit, sed quia consequuntur magni dolores eos...</p>
  </div>
  <div class="btn hero-btn abs"><div class="mark"></div><span>GET STARTED</span></div>
  <div class="dots abs"><i></i><i class="on"></i><i></i></div>
</section>

<section>
  <div class="about-block abs"></div>
  <div class="about-photo abs" role="img" aria-label="Professional woman in a blazer reading a tablet in a bright office"></div>
  <div class="about-copy abs">
    <div class="eyebrow" style="font-size:17px">About</div>
    <h2>THORNFIELD MARSH, LLC</h2>
    <p class="body-text">It is a long established fact that a reader will be distracted by the reada ble content of a page when looking at its layout. The point of using Lorem Ipsum is that it has a more-or-less normal distribution of letters, as opposed to using 'Content here, content here', making it look like readable English. Many desktop publishing packages and web page editors now use Lorem Ipsum uncover many web sites still in their infancy.</p>
    <p class="body-text">The point of using Lorem Ipsum is that it has a more-or-less normal distribution of letters, as opposed to using 'Content here, content here', making it look like readable English. Many desktop packages and web page editors now use.....</p>
    <div class="btn" style="width:178px;margin-top:4px"><div class="mark"></div><span>READ MORE</span></div>
  </div>
</section>

<section class="attorneys abs">
  <div class="eyebrow abs center" style="top:34px">Our Lawyers</div>
  <h2 class="section-title abs center" style="top:60px">Meet Our Attorneys</h2>
  <div class="card abs" style="left:111px"><div class="portrait" role="img" aria-label="Portrait of Leonard Thornfield"></div><h4>Leonard Thornfield</h4><div class="role">Attorney</div><div class="plus abs">+</div></div>
  <div class="card gold abs" style="left:446px"><div class="portrait" role="img" aria-label="Portrait of Brent Marsh"></div><h4>Brent Marsh</h4><div class="role">Attorney</div><div class="socials"><i></i><i></i><i></i><i></i></div><div class="plus abs">+</div></div>
  <div class="card abs" style="left:779px"><div class="portrait" role="img" aria-label="Portrait of Melinda Carrow"></div><h4>Melinda Carrow</h4><div class="role">Legal Assistant</div><div class="plus abs">+</div></div>
</section>

<section class="lit abs">
  <svg class="lit-photo abs" viewBox="0 0 1200 474" role="img" aria-label="Attorney addressing a wood-panelled courtroom">
    <defs><linearGradient id="court" x1="0" y1="0" x2="1" y2="1"><stop offset="0" stop-color="#7a4f2c"/><stop offset="1" stop-color="#2c1c12"/></linearGradient></defs>
    <polygon points="748,0 1200,0 1200,474 622,474" fill="url(#court)"/>
    <polygon points="740,0 748,0 622,474 614,474" fill="#fff"/>
  </svg>
  <div class="lit-copy abs">
    <h6>THORNFIELD MARSH</h6>
    <h2>MULTIDISTRICT LITIGATION</h2>
    <p class="body-text">It is a long established fact that a reader will be distracted by the reada ble content of a page when looking at its layout. The point of using Lorem Ipsum is that it has a more-or-less normal distribution of letters, as opposed to using 'Content here, content here', making it look like readable English. Many desktop publishing packages and web page editors now use Lorem Ipsum uncover many web sites still in their infancy. Sed ut perspiciatis unde omnis iste natus error sit voluptatem accusantium doloremque laudantium, totam quasi architecto beatae vitae dicta sunt explicabo.</p>
  </div>
  <div class="btn lit-btn abs" style="width:178px"><div class="mark"></div><span>READ MORE</span></div>
</section>

<section>
  <div class="eyebrow abs center" style="top:2464px">Thornfield Marsh</div>
  <h2 class="section-title abs center" style="top:2488px">Latest Blog</h2>
  <article class="post abs" style="left:111px"><div class="img" role="img" aria-label="Team of lawyers reviewing work at a laptop"></div><div class="box"><div class="date">08 Apr 2025</div><h5>Nemo enim ipsam voluptat</h5><p>Neque porro quisquam est, qui dolorem ipsum quia dolor sit amet consectetur adipisci velit</p><div class="meta">by admin / 1 week ago<i><svg width="12" height="12" viewBox="0 0 12 12"><path d="M2 1l9 5-9 5z" fill="none" stroke="#aaa"/></svg></i></div></div></article>
  <article class="post abs" style="left:446px"><div class="img" role="img" aria-label="Courtroom with judge's gavel in the foreground"></div><div class="box"><div class="date">08 Apr 2025</div><h5>Nemo enim ipsam voluptat</h5><p>Neque porro quisquam est, qui dolorem ipsum quia dolor sit amet consectetur adipisci velit</p><div class="meta">by admin / 1 week ago<i><svg width="12" height="12" viewBox="0 0 12 12"><path d="M2 1l9 5-9 5z" fill="none" stroke="#aaa"/></svg></i></div></div></article>
  <article class="post abs" style="left:780px"><div class="img" style="background:linear-gradient(160deg,#b9b3a8,#4a4136)" role="img" aria-label="Business meeting in a high-rise office at sunset"></div><div class="box"><div class="date">08 Apr 2025</div><h5>Nemo enim ipsam voluptat</h5><p>Neque porro quisquam est, qui dolorem ipsum quia dolor sit amet consectetur adipisci velit</p><div class="meta">by admin / 1 week ago<i><svg width="12" height="12" viewBox="0 0 12 12"><path d="M2 1l9 5-9 5z" fill="none" stroke="#aaa"/></svg></i></div></div></article>
</section>

<section class="testi abs">
  <div class="eyebrow abs center" style="top:38px">Thornfield Marsh</div>
  <h2 class="section-title abs center" style="top:62px">Our Testimonials</h2>
  <div class="arrow abs" style="left:61px"><svg width="10" height="14" viewBox="0 0 10 14"><path d="M8 1L2 7l6 6" fill="none" stroke="#999" stroke-width="1.5"/></svg></div>
  <div class="quote abs" style="left:111px"><p>"Nemo enim ipsam voluptatem quia voluptas sit aspernatur aut odit aut fugit, sed quia consequuntur magni dolores eos qui ratione voluptatem sequi nesciunt. Neque porro quis quia consequuntur sed quia non numquam."</p><div class="who">Arlen Peck</div><div class="stars">★★★★★</div><div class="qmark abs">”</div></div>
  <div class="quote abs" style="left:613px"><p>"Nemo enim ipsam voluptatem quia voluptas sit aspernatur aut odit aut fugit, sed quia consequuntur magni dolores eos qui ratione voluptatem sequi nesciunt. Neque porro quis quia consequuntur sed quia non numquam."</p><div class="who">Arlen Peck</div><div class="stars">★★★★★</div><div class="qmark abs">”</div></div>
  <div class="arrow abs" style="left:1104px"><svg width="10" height="14" viewBox="0 0 10 14"><path d="M2 1l6 6-6 6" fill="none" stroke="#999" stroke-width="1.5"/></svg></div>
</section>

<footer class="footer abs">
  <h3 class="abs" style="top:34px;left:114px">Get In Touch</h3>
  <div class="field abs" style="top:84px;left:114px;width:180px">First Name :</div>
  <div class="field abs" style="top:84px;left:304px;width:181px">Last Name :</div>
  <div class="field abs" style="top:128px;left:114px;width:180px">Email :</div>
  <div class="field abs" style="top:128px;left:304px;width:181px">Phone :</div>
  <div class="field abs" style="top:172px;left:114px;width:371px;height:54px">Message :</div>
  <div class="submit abs">SUBMIT</div>

  <h3 class="abs" style="top:34px;left:563px">Contact Us</h3>
  <div class="c-item abs" style="top:82px"><div class="ic"><svg width="16" height="18" viewBox="0 0 16 20"><path d="M8 1a6 6 0 0 0-6 6c0 5 6 12 6 12s6-7 6-12a6 6 0 0 0-6-6z" fill="none" stroke="#fff" stroke-width="1.8"/><circle cx="8" cy="7" r="2" fill="#fff"/></svg></div><div><b>ADDRESS</b><span>42 Alder Row #3<br>Brookvale, 02914</span></div></div>
  <div class="c-item abs" style="top:158px"><div class="ic"><svg width="16" height="16" viewBox="0 0 24 24"><path fill="#fff" d="M6.6 10.8a15 15 0 0 0 6.6 6.6l2.2-2.2c.3-.3.7-.4 1-.2 1.1.4 2.3.6 3.6.6.6 0 1 .4 1 1V20c0 .6-.4 1-1 1A17 17 0 0 1 3 4c0-.6.4-1 1-1h3.5c.6 0 1 .4 1 1 0 1.3.2 2.5.6 3.6.1.3 0 .7-.2 1z"/></svg></div><div><b>PHONE</b><span>555-018-2746</span></div></div>
  <div class="c-item abs" style="top:222px"><div class="ic"><svg width="18" height="14" viewBox="0 0 20 14"><rect x="1" y="1" width="18" height="12" fill="none" stroke="#fff" stroke-width="1.6"/><path d="M1 1l9 7 9-7" fill="none" stroke="#fff" stroke-width="1.6"/></svg></div><div><b>EMAIL</b><span>info@thornfieldmarsh.com</span></div></div>

  <div class="flogo abs"><div class="sq"></div><b>THORNFIELD MARSH, LLC</b></div>
  <div class="fsoc abs"><i></i><i></i><i></i><i></i><i></i></div>

  <div class="copy abs center">© Copyright 2025 Thornfield Marsh, LLC.All Rights Reserved</div>
</footer>

</body>
</html>
```